Business Card / Appointment Card for Physician

On one side it should give the logo, address, and contact information, and on the other side it should br an Appointment card.

One Side:
Logo (see attached files)
Board Certified American Orthopedic Surgery

1487 Harrowgate Ave.
Suite KM7
Bronx, NY 10527
Tel: (718) 552 - 1948
Fax: (718) 552 - 7210

628 Fourth Ave.
Suite 42
New York, NY 10087
Tel: (212) 734 - 2815

Second Side:
Appointment
give them a choice of Bronx or Mahattan office
For:
Date:
Time:

If you are unable to keep your appointment, please call (718) 263-5102 24hrs in advance.

Target Market(s)

People that need orthopedic surgery

Industry/Entity Type

Business

Contact Information for Business Card

smart and attractive

Requirements
Must have
• logo
• contact information on one side, appointment information on the other

```html
<!DOCTYPE html>
<html lang="en">
<head>
<meta charset="utf-8">
<title>Daniel R. Ashcombe MD PC – Business &amp; Appointment Card</title>
<link href="https://fonts.googleapis.com/css2?family=Open+Sans:wght@400;600;700&display=swap" rel="stylesheet">
<style>
  :root {
    --canvas-bg: #8f8f8f;
    --card-bg: #ffffff;
    --brand-cyan: #1ec0ee;
    --brand-cyan-deep: #00aeef;
    --brand-navy: #1f6fb2;
    --text-dark: #3a3a3a;
    --rule-grey: #555555;
    --decor-tint: #f2f4ee;
  }
  * { margin: 0; padding: 0; box-sizing: border-box; }
  html, body { width: 1200px; height: 1000px; overflow: hidden; }
  body {
    background: var(--canvas-bg);
    font-family: "Open Sans", Arial, sans-serif;
    color: var(--text-dark);
    position: relative;
  }
  .card {
    position: absolute;
    left: 348px;
    width: 515px;
    height: 302px;
    background: var(--card-bg);
    overflow: hidden;
  }
  .card--front { top: 151px; }
  .card--back { top: 530px; }

  /* Front */
  .front-illustration { position: absolute; left: 0; top: 0; width: 140px; height: 302px; }
  .front-info { position: absolute; left: 224px; top: 0; }
  .practice-name {
    position: absolute; top: 70px; left: 0; white-space: nowrap;
    font-size: 14px; font-weight: 400; letter-spacing: 0.3px;
    color: var(--brand-navy);
  }
  .certification {
    position: absolute; top: 101px; left: 0; white-space: nowrap;
    font-size: 12.5px;
  }
  .accent-rule {
    position: absolute; top: 123px; left: 0;
    width: 35px; height: 2px; background: var(--brand-cyan);
  }
  .office { position: absolute; left: 0; font-size: 12.3px; line-height: 15.3px; white-space: nowrap; }
  .office--bronx { top: 136px; }
  .office--manhattan { top: 220px; }
  .label { color: var(--brand-cyan); }

  /* Back */
  .back-decor { position: absolute; right: 0; top: 0; width: 180px; height: 302px; }
  .appt-title {
    position: absolute; top: 30px; left: 0; width: 515px; text-align: center;
    font-size: 20px; font-weight: 700; color: var(--brand-cyan); letter-spacing: 0.3px;
  }
  .appt-office {
    position: absolute; top: 73px; left: 0; width: 515px; text-align: center;
    font-size: 14px; font-weight: 600; color: var(--brand-navy);
  }
  .appt-field { position: absolute; left: 33px; width: 447px; height: 16px; font-size: 12px; }
  .appt-field span { position: absolute; left: 0; top: 0; }
  .appt-field::after {
    content: ""; position: absolute; left: 36px; right: 0; top: 13px;
    border-bottom: 1px solid var(--rule-grey);
  }
  .appt-field--for { top: 123px; }
  .appt-field--time { top: 160px; }
  .appt-field--date { top: 198px; }
  .appt-note {
    position: absolute; top: 254px; left: 0; width: 510px; text-align: center;
    font-size: 12.3px; line-height: 15px;
  }
</style>
</head>
<body>
  <section class="card card--front">
    <svg class="front-illustration" viewBox="0 0 140 302" role="img" aria-label="Stylised knee joint illustration in blue tones">
      <defs>
        <linearGradient id="kneeFill" x1="0" y1="0" x2="0" y2="1">
          <stop offset="0" stop-color="#22c6f4"/>
          <stop offset="1" stop-color="#00aeef"/>
        </linearGradient>
      </defs>
      <path d="M0 0 H78 C95 30 125 60 136 100 C142 140 120 200 108 240 C102 265 104 285 106 302 H0 Z" fill="url(#kneeFill)"/>
    </svg>
    <div class="front-info">
      <div class="practice-name">DANIEL R. ASHCOMBE MD PC</div>
      <div class="certification">Board Certified American Orthopedic Surgery</div>
      <div class="accent-rule"></div>
      <address class="office office--bronx" style="font-style:normal">
        1487 Harrowgate Ave.<br>
        Suite KM7<br>
        Bronx, NY 10527<br>
        <span class="label">Tel:</span> (718) 552 - 1948<br>
        <span class="label">Fax:</span> (718) 552 - 7210
      </address>
      <address class="office office--manhattan" style="font-style:normal">
        628 Fourth Ave.<br>
        Suite 42<br>
        New York, NY 10087<br>
        <span class="label">Tel:</span> (212) 734 - 2815
      </address>
    </div>
  </section>

  <section class="card card--back">
    <svg class="back-decor" viewBox="0 0 180 302" aria-hidden="true">
      <path d="M180 0 H150 C80 30 40 110 30 180 C24 230 30 270 40 302 H180 Z" fill="var(--decor-tint)"/>
    </svg>
    <h1 class="appt-title">APPOINTMENT</h1>
    <h2 class="appt-office">Mahattan office</h2>
    <div class="appt-field appt-field--for"><span>For:</span></div>
    <div class="appt-field appt-field--time"><span>Time:</span></div>
    <div class="appt-field appt-field--date"><span>Date:</span></div>
    <p class="appt-note">If you are unable to keep your appointment,<br>please call (718) 263-5102 24hrs in advance.</p>
  </section>
</body>
</html>
```